I need to redesign this website. Modern Fun Professional Redesign For www.JollyPerkHub.com = New Name www.ClaimVouchly.com

Use existing content as it is on website exactly and we will revise after initial mock ups.

The new name will be ClaimVouchly.com please make a quick logo for this site too while redesigning.

Make it look like an official website....

Target Market(s)

Consumers that are redeeming certificates that businesses gave to them as a gift for customer loyalty,e tc.

Industry/Entity Type

It Professional

Logo Text

www.ClaimVouchly.com

Number of Pages Required

4 page

Colors

Designer to choose colors to be used in the design.

Requirements
Must have
• Must look professional, build trust and credibility.
Nice to have
• open
Should not have
• open

```html
<!DOCTYPE html>
<html lang="en">
<head>
<meta charset="utf-8">
<title>ClaimVouchly.com – Redeem Your Certificate</title>
<link href="https://fonts.googleapis.com/css2?family=Open+Sans:ital,wght@0,400;0,600;0,700;1,400;1,700&display=swap" rel="stylesheet">
<style>
:root{
  --blue:#1a9fdb;
  --green:#8cc63f;
  --ink:#222222;
  --text:#3a3a3a;
  --muted:#555555;
  --rule:#1f1f1f;
  --band:#e8e8e8;
  --footer:#3c3d3f;
  --white:#ffffff;
}
*{box-sizing:border-box;margin:0;padding:0}
html,body{width:1200px;height:2514px;overflow:hidden;background:var(--white)}
body{position:relative;font-family:"Open Sans",Arial,sans-serif;color:var(--text)}
.abs{position:absolute}
a{color:inherit;text-decoration:none}

/* header */
.site-header{left:0;top:0;width:1200px;height:136px;border-bottom:2px solid var(--rule)}
.brand{display:flex;align-items:center;gap:12px}
.brand-mark{width:46px;height:46px;background:var(--blue);border-radius:6px}
.brand-name{font-weight:600;font-size:40px;color:var(--green);letter-spacing:-.5px}
.site-header .brand{left:87px;top:44px}
.top-links{right:88px;top:66px;display:flex;gap:30px;font-size:16px;color:var(--ink);letter-spacing:.3px}
.top-links span{display:flex;align-items:center;gap:9px}

/* nav */
.main-nav{left:0;top:137px;width:1200px;height:56px}
.main-nav ul{list-style:none}
.nav-item{top:151px;display:flex;align-items:center;gap:8px;font-size:17px;color:var(--ink)}
.social-row{left:877px;top:150px;display:flex;align-items:center;gap:10px;color:var(--blue);font-size:22px}
.social-dot{width:20px;height:20px;border-radius:50%;background:var(--blue)}

/* hero */
.hero{left:0;top:193px;width:1200px;height:514px;
  background:linear-gradient(180deg,#8f8c88 0%,#a7a39c 35%,#6b6a67 70%,#3b3a38 100%)}
.redeem-panel{left:87px;top:349px;width:1024px;height:214px;background:rgba(255,255,255,.82);text-align:center}
.redeem-title{position:absolute;left:0;right:0;top:29px;font-size:25px;font-weight:700;color:var(--blue);letter-spacing:.4px}
.redeem-sub{position:absolute;left:0;right:0;top:70px;font-size:16.5px;color:var(--ink);letter-spacing:.3px}
.cert-input{position:absolute;left:200px;top:114px;width:480px;height:54px;border:3px solid var(--blue);border-radius:4px;background:var(--white)}
.go-btn{position:absolute;left:689px;top:114px;width:137px;height:54px;background:var(--green);color:var(--white);font-size:26px;font-weight:600;line-height:54px}

/* welcome */
.section-title{left:0;width:1200px;text-align:center;font-size:30px;font-weight:600;letter-spacing:.3px}
.c-blue{color:var(--blue)}
.c-green{color:var(--green)}
.welcome-lead{left:0;width:1200px;top:843px;text-align:center;font-size:21px;font-weight:700;font-style:italic;color:var(--ink)}
.welcome-text{left:120px;width:960px;top:888px;text-align:center;font-size:17.5px;line-height:26px;color:var(--text)}
.welcome-text em{font-weight:700;color:var(--ink)}
.divider-line{left:598px;top:1002px;width:2px;height:54px;background:var(--ink)}
.divider-dot{left:594px;top:1053px;width:10px;height:10px;border-radius:50%;background:var(--ink)}

/* products */
.photo{background:linear-gradient(135deg,#6fb4e8,#d6a25a)}
.photo-tower{left:111px;top:1146px;width:241px;height:347px;background:linear-gradient(180deg,#3d8fe0 0%,#9cc8ef 40%,#e08a3f 65%,#5a4a3c 100%)}
.photo-bikes{left:360px;top:1146px;width:240px;height:170px;background:linear-gradient(180deg,#7ab5e6 0%,#bcd7ea 40%,#8aa84a 65%,#6f8d2f 100%)}
.photo-sea{left:360px;top:1324px;width:240px;height:169px;background:linear-gradient(180deg,#8ac3ea 0%,#2aa6cf 45%,#25b8c8 70%,#5f8f3d 100%)}
.exp-title{left:645px;top:1196px;font-size:33px;color:var(--ink)}
.exp-sub{left:645px;top:1241px;font-size:22px;font-weight:600;color:var(--ink)}
.exp-text{left:645px;top:1277px;width:480px;font-size:15.5px;line-height:24px;color:var(--text)}
.see-more{left:647px;top:1388px;width:149px;height:40px;border:2px solid var(--blue);color:var(--blue);font-size:17px;text-align:center;line-height:36px}

/* testimonials */
.testimonials{left:0;top:1604px;width:1200px;height:421px;background:var(--band)}
.avatar{left:550px;top:1733px;width:100px;height:100px;border-radius:50%;background:linear-gradient(180deg,#b88f6a,#d9b79a 50%,#5a7fa8)}
.quote{left:0;width:1200px;top:1858px;text-align:center;font-size:18px;line-height:25px;color:var(--ink)}
.quote-author{left:0;width:1200px;top:1925px;text-align:center;font-size:26px;color:var(--blue);text-decoration:underline;text-underline-offset:5px}

/* footer */
.site-footer{left:0;top:2025px;width:1200px;height:439px;background:linear-gradient(180deg,#3a3b3d 0%,#444547 60%,#56585a 100%)}
.site-footer .brand{left:87px;top:2077px}
.footer-about{left:86px;top:2164px;width:300px;font-size:15.5px;line-height:21px;color:var(--white)}
.contact-row{left:88px;display:flex;gap:20px;font-size:13.5px;line-height:16px;color:var(--white)}
.contact-row svg{flex:none}
.col-title{top:2097px;font-size:22px;font-weight:600;color:var(--green)}
.footer-list{list-style:none;font-size:15.5px;color:var(--white)}
.footer-list li{height:31px;display:flex;align-items:center;gap:12px}
.bullet-arrow{width:0;height:0;border-top:5px solid transparent;border-bottom:5px solid transparent;border-left:6px solid var(--blue)}
.bullet-square{width:13px;height:13px;background:var(--blue);border-radius:2px}
.field{left:805px;width:313px;border:1.5px solid #d8d8d8;background:#2f3032;color:var(--white);font-size:15px;padding:5px 16px}
.send-btn{left:977px;top:2400px;width:139px;height:37px;background:var(--green);color:var(--white);font-size:14px;text-align:center;line-height:37px}
.copyright{left:0;top:2464px;width:1200px;height:50px;background:var(--blue);color:var(--white);font-size:12px;text-align:center;line-height:50px}
</style>
</head>
<body>

<header class="site-header abs">
  <div class="brand abs"><span class="brand-mark"></span><span class="brand-name">ClaimVouchly</span></div>
  <div class="top-links abs">
    <span>EXPERIENCE &amp; ACTIVITIES</span>
    <span><svg width="14" height="14" viewBox="0 0 14 14"><rect width="14" height="14" rx="2" fill="#8cc63f"/><path d="M4 3.5c.5 2.8 2.3 5 5 6.5l1-1.2 1.5 1-1 1.5C6.5 10.5 3.5 7.5 2.8 4.5L4 3.5z" fill="#fff"/></svg>CUSTOMER SUPPORT</span>
  </div>
</header>

<nav class="main-nav abs" aria-label="Main">
  <ul>
    <li class="nav-item abs" style="left:92px"><svg width="15" height="14" viewBox="0 0 15 14"><path d="M7.5 0L15 6.5h-2.2V14H9.3V9.5H5.7V14H2.2V6.5H0z" fill="#1a9fdb"/></svg>HOME</li>
    <li class="nav-item abs" style="left:198px"><svg width="15" height="15" viewBox="0 0 15 15"><circle cx="7.5" cy="7.5" r="7.5" fill="#1a9fdb"/><text x="7.5" y="11.5" font-size="11" font-weight="700" text-anchor="middle" fill="#fff" font-family="Open Sans,sans-serif">?</text></svg>ABOUT US</li>
    <li class="nav-item abs" style="left:340px"><svg width="17" height="14" viewBox="0 0 17 14"><ellipse cx="8" cy="6" rx="8" ry="5.5" fill="#1a9fdb"/><path d="M3 9l-1 5 5-3z" fill="#1a9fdb"/></svg>TESTIMONIALS</li>
    <li class="nav-item abs" style="left:518px"><svg width="16" height="15" viewBox="0 0 16 15"><rect x="1" y="3" width="11" height="11" fill="none" stroke="#1a9fdb" stroke-width="1.6"/><path d="M6 9l8-8 1.5 1.5-8 8H6z" fill="#1a9fdb"/></svg>TERMS</li>
    <li class="nav-item abs" style="left:634px"><svg width="13" height="14" viewBox="0 0 13 14"><path d="M2.5 0.5l3 3-1.5 2c1 2 2.5 3.5 4.5 4.5l2-1.5 2.5 3-2 2C5.5 13 0 7.5 0.5 2.5z" fill="#1a9fdb"/></svg>CONTACT&nbsp; US</li>
  </ul>
  <div class="social-row abs" aria-label="Social links">
    <span class="social-dot"></span>/<span class="social-dot"></span>/<span class="social-dot"></span>/<span class="social-dot"></span>/<span class="social-dot"></span>
  </div>
</nav>

<section class="hero abs" role="img" aria-label="Photo of a smiling couple walking on a beach with colourful confetti in the air"></section>
<form class="redeem-panel abs">
  <h1 class="redeem-title">PLEASE ENTER A VALID CERTIFICATE ID IN THE FORM BELOW</h1>
  <p class="redeem-sub">TO REDEEM YOUR CERTIFICATE AND TO VIEW FAQ'S, TERMS AND LOCATIONS.</p>
  <div class="cert-input"></div>
  <div class="go-btn">GO</div>
</form>

<section class="welcome">
  <h2 class="section-title abs" style="top:795px"><span class="c-blue">WELCOME TO </span><span class="c-green">CLAIM VOUCHLY</span></h2>
  <p class="welcome-lead abs">ClaimVouchly.com is a leading company in travel certificate fulfillment.</p>
  <p class="welcome-text abs">Our goal is to make it easy for you to redeem your certificate and our philosophy is this: <em>"What good is it to receive a gift certificate if you can't use it?".</em> If you have any questions about how to redeem a certain certificate, please contact us.<br>We are here to help.</p>
  <div class="divider-line abs"></div>
  <div class="divider-dot abs"></div>
</section>

<section class="products">
  <h2 class="section-title abs" style="top:1073px"><span class="c-green">PRODUCTS </span><span class="c-blue">&amp; SERVICES</span></h2>
  <div class="photo-tower abs" role="img" aria-label="Photo of a red pagoda at sunrise above a city"></div>
  <div class="photo-bikes abs" role="img" aria-label="Photo of a couple on bicycles in a green meadow"></div>
  <div class="photo-sea abs" role="img" aria-label="Photo of a traveller looking out over a turquoise bay"></div>
  <h3 class="exp-title abs">Experiences</h3>
  <h4 class="exp-sub abs">Hand-Picked Experiences For All Occasions</h4>
  <p class="exp-text abs">Imagine rewarding someone with the thrill of driving a fast car, the peace of a relaxing spa day, a sumptuous dinner on a yacht or the spectacle of flying in a hot air balloon. ClaimVouchly has curated 6000+ experiences, something for everyone.</p>
  <a class="see-more abs">See More</a>
</section>

<section class="testimonials abs"></section>
<h2 class="section-title abs" style="top:1670px;display:flex;justify-content:center;align-items:center;gap:10px">
  <svg width="34" height="28" viewBox="0 0 34 28"><path d="M0 14C0 6 4 1 12 0v5c-4 1-5 4-5 7h5v16H0zM18 14c0-8 4-13 12-14v5c-4 1-5 4-5 7h5v16H18z" fill="#8cc63f"/></svg>
  <span class="c-blue">TESTIMONIALS</span>
</h2>
<div class="avatar abs" role="img" aria-label="Portrait of the customer giving the testimonial"></div>
<p class="quote abs">"Helen was a "saving grace.' She followed up and helped me book the vacation and air fare.<br>Helen was positive and did everything she promised to do. "</p>
<p class="quote-author abs">- Maria T.</p>

<footer class="site-footer abs" role="img" aria-label="Dim photo of a traveller overlooking a city skyline"></footer>
<div class="brand abs" style="left:87px;top:2082px"><span class="brand-mark"></span><span class="brand-name">ClaimVouchly</span></div>
<p class="footer-about abs">www.ClaimVouchly.com is a leading company in travel certificate fulfillment</p>
<div class="contact-row abs" style="top:2228px">
  <svg width="12" height="17" viewBox="0 0 12 17"><path d="M6 0a6 6 0 016 6c0 4.5-6 11-6 11S0 10.5 0 6a6 6 0 016-6z" fill="#1a9fdb"/><circle cx="6" cy="6" r="2.3" fill="#3c3d3f"/></svg>
  <span>The Voucher Desk<br>2150 Maple Grove Ave Ste 12<br>Brookfield, CA 90210</span>
</div>
<div class="contact-row abs" style="top:2291px">
  <svg width="14" height="15" viewBox="0 0 13 14"><path d="M2.5 0.5l3 3-1.5 2c1 2 2.5 3.5 4.5 4.5l2-1.5 2.5 3-2 2C5.5 13 0 7.5 0.5 2.5z" fill="#1a9fdb"/></svg>
  <span>+100 555 0142</span>
</div>
<div class="contact-row abs" style="top:2330px">
  <svg width="16" height="12" viewBox="0 0 16 12"><rect width="16" height="12" rx="1" fill="#1a9fdb"/><path d="M0 1l8 6 8-6" fill="none" stroke="#3c3d3f" stroke-width="1.4"/></svg>
  <span>info@claimvouchly.com</span>
</div>

<h3 class="col-title abs" style="left:422px">Navigation</h3>
<ul class="footer-list abs" style="left:422px;top:2159px">
  <li><span class="bullet-arrow"></span>Home</li>
  <li><span class="bullet-arrow"></span>Contact Us</li>
  <li><span class="bullet-arrow"></span>Testimonials</li>
  <li><span class="bullet-arrow"></span>Terms</li>
</ul>

<h3 class="col-title abs" style="left:612px">Follow Us</h3>
<ul class="footer-list abs" style="left:612px;top:2159px">
  <li><span class="bullet-square"></span>ChatterPage</li>
  <li><span class="bullet-square"></span>ClipStream</li>
  <li><span class="bullet-square"></span>SnapGallery</li>
  <li><span class="bullet-square"></span>Chirper</li>
</ul>

<h3 class="col-title abs" style="left:805px">Have Questions ?</h3>
<div class="field abs" style="top:2172px;height:35px">Your Name</div>
<div class="field abs" style="top:2216px;height:35px">Your Email</div>
<div class="field abs" style="top:2261px;height:119px">Massage</div>
<div class="send-btn abs">SEND</div>

<div class="copyright abs">Copyright © 2014. ClaimVouchly. All Rights Reserved.</div>

</body>
</html>
```